Outdoor sign for Brindle Auto Restoration

I need a horizontal 4'x 8' outdoor roadside sign for my classic auto restoration business. I have uploaded colors and our logo. Needs the Brindle name, a prominent Classic AUTO RESTORATION, phone number and website. We rebuild and restore vintage cars, trucks and 4x4s. I'd like something clean but possibly retro. Classic Auto Restoration is more important than the Brindle name. It needs to be visible and readable from the street. NO CLIP ART

Target Market(s)

Customers who need their vintage care restored or upgraded. Men and women ages 25-75

Industry/Entity Type

Automotive

Colors
FFC000
F8CF3A
FAE287
FDF2CF
FEFAEE

Requirements
Must have
• Legible. Bright. Readable as a backlit 4' x 8' large horizontal sign (roughly 120cm X 240cm)
Nice to have
• Use of the Brindle logo/type, Complete or Classic before prominent AUTO RESTORATION
Should not have
• Clip art of old cars or icons. And we don't want the Brindle Logo from the website because it wont be legible from the road. I have included the Illustrator file for Brindle text in the uploads

```html
<!DOCTYPE html>
<html lang="en">
<head>
<meta charset="utf-8">
<title>Brindle Auto Restoration – Roadside Sign</title>
<link rel="stylesheet" href="https://fonts.googleapis.com/css2?family=Alfa+Slab+One&family=Oswald:wght@700&display=swap">
<style>
  :root {
    --paper: #ffffff;
    --sign-black: #231f20;
    --gold: #f8cf3a;
    --amber: #f7a81b;
    --border-gold: #d9b82a;
    --headline-white: #ffffff;
    --ink: #231f20;
  }
  html, body {
    margin: 0;
    padding: 0;
    width: 1200px;
    height: 849px;
    overflow: hidden;
    background: var(--paper);
  }
  .canvas { display: block; width: 1200px; height: 849px; }
  .sign-frame { fill: var(--sign-black); }
  .checker-border { fill: var(--border-gold); }
  .sign-panel { fill: var(--sign-black); }
  .info-band { fill: var(--gold); }
  .headline {
    font-family: "Oswald", sans-serif;
    font-weight: 700;
  }
  .headline-auto {
    font-size: 170px;
    fill: var(--gold);
  }
  .headline-restoration {
    font-size: 88px;
    fill: var(--headline-white);
  }
  .brand-name {
    font-family: "Oswald", sans-serif;
    font-weight: 700;
    font-size: 58px;
    fill: var(--amber);
  }
  .contact-line {
    font-family: "Alfa Slab One", serif;
    font-size: 22px;
    fill: var(--ink);
  }
</style>
</head>
<body>
<svg class="canvas" viewBox="0 0 1200 849" xmlns="http://www.w3.org/2000/svg">
  <!-- sign body -->
  <rect class="sign-frame" x="159" y="156" width="882" height="537"/>
  <g role="img" aria-label="Checkered flag border in yellow and black">
    <rect class="checker-border" x="163" y="160" width="874" height="456"/>
  </g>
  <rect class="sign-panel" x="197" y="196" width="806" height="420"/>

  <!-- headline -->
  <text class="headline headline-auto" x="600" y="410" text-anchor="middle" textLength="560" lengthAdjust="spacingAndGlyphs">AUTO</text>
  <text class="headline headline-restoration" x="600" y="500" text-anchor="middle" textLength="640" lengthAdjust="spacingAndGlyphs">RESTORATION</text>

  <!-- brand -->
  <text class="brand-name" x="951" y="575" text-anchor="end">BRINDLE</text>

  <!-- contact band -->
  <rect class="info-band" x="159" y="616" width="882" height="72"/>
  <text class="contact-line" x="217" y="659" textLength="441" lengthAdjust="spacingAndGlyphs">BRINDLEAUTOWORKS.COM</text>
  <text class="contact-line" x="772" y="659" textLength="198" lengthAdjust="spacingAndGlyphs">501-555-0142</text>
</svg>
</body>
</html>
```